VeroTide Powerpoint design

We've recently redesigned our logos and would like a single presentation format that we can easily interchange the logos attached into. The presentation will be used for general company sales information. The group is called VeroTide and has 2 companies, k7gridworks and Quiet Harbor. We're an IT services company who specialises in Broadband and general network services.

Target Market(s)

Professional

```html
<!DOCTYPE html>
<html lang="en">
<head>
<meta charset="utf-8">
<title>VeroTide Presentation Template</title>
<link href="https://fonts.googleapis.com/css2?family=Poppins:ital,wght@0,300;0,400;0,500;0,600;0,700;1,400&display=swap" rel="stylesheet">
<style>
:root{
  --blue:#1fa3de;
  --blue-light:#5cc1ec;
  --navy:#1b5f9a;
  --red:#d8222a;
  --ink:#333;
  --grey:#8a8a8a;
  --soft:#e9eaec;
  --canvas:#cbccce;
  --white:#fff;
}
*{box-sizing:border-box;margin:0;padding:0}
html,body{width:1200px;height:850px;overflow:hidden}
body{background:var(--canvas);font-family:'Poppins',sans-serif;color:var(--ink);position:relative}
.slide{position:absolute;width:176px;height:99px;background:var(--white);box-shadow:1px 2px 4px rgba(0,0,0,.28);overflow:hidden}
.c1{left:54px}.c2{left:267px}.c3{left:490px}.c4{left:717px}.c5{left:934px}
.r1{top:57px}.r2{top:190px}.r3{top:313px}.r4{top:435px}.r5{top:569px}.r6{top:710px}
.footbar{position:absolute;left:0;right:0;bottom:0;height:5px;background:var(--blue)}
.brand{position:absolute;left:6px;bottom:0;height:8px;background:var(--white);padding:0 3px;font-size:4.4px;font-weight:600;color:var(--ink);display:flex;align-items:center;gap:1.5px}
.brand::before{content:"";width:3.4px;height:3.4px;border-radius:50%;background:var(--blue)}
.page{position:absolute;right:8px;bottom:1.4px;font-size:1.8px;color:var(--white)}
.title{position:absolute;top:9px;left:0;right:0;text-align:center;font-size:4.6px;font-weight:600;color:var(--blue)}
.title::before{content:"";display:block;width:6px;height:.5px;background:var(--blue);margin:0 auto 1.2px}
.title.left{text-align:left}
.title.left::before{margin:0 0 1.2px}
.sub{position:absolute;left:0;right:0;text-align:center;font-size:1.8px;color:#555}
.p{font-size:1.7px;line-height:2.3px;color:#555}
.h{font-size:2.6px;font-weight:600;color:var(--blue)}
.abs{position:absolute}
.photo{position:absolute}
.center{text-align:center}
svg{position:absolute;overflow:visible}

/* cover */
.cover-top{position:absolute;left:0;top:0;right:0;height:34px;background:var(--white)}
.cover-brand{position:absolute;left:10px;top:8px;font-size:10px;font-weight:600;color:var(--ink);display:flex;align-items:center;gap:3px}
.cover-brand::before{content:"";width:8px;height:8px;border-radius:50%;background:var(--blue)}
.cover-band{position:absolute;left:0;right:0;top:34px;bottom:0;background:linear-gradient(120deg,#2aa3dd,#5fc0ea 60%,#3aaee2)}
.cover-title{position:absolute;left:9px;top:46px;font-size:5.6px;font-weight:300;color:var(--white);letter-spacing:.1px}
.cover-sub{position:absolute;left:9px;top:55px;font-size:4px;font-weight:600;color:var(--white)}
.cover-date,.cover-web{position:absolute;bottom:5px;font-size:2px;color:var(--white)}
.cover-date{left:9px}.cover-web{right:9px}

/* contents */
.toc{position:absolute;width:42px;font-size:2.1px;display:flex;justify-content:space-between;border-bottom:.4px solid var(--blue);padding-bottom:.6px}
.toc b{font-weight:600}

/* vision */
.red-band{position:absolute;left:10px;right:0;top:27px;height:33px;background:var(--red);padding:4px 9px;font-size:2.9px;line-height:4.7px;color:var(--white);font-style:italic}

/* mission */
.mblock{position:absolute;width:44px;height:26px;padding:2px 3px;text-align:center}
.mblock.shade{background:var(--soft);box-shadow:.5px .5px 1.5px rgba(0,0,0,.2)}

/* stat boxes */
.stat{position:absolute;height:12px;width:25px;background:var(--soft);padding:1.5px 2px;font-size:2.1px;line-height:2.6px;color:#444}
.stat b{display:block;color:var(--blue);font-weight:600}
.stat.red{background:var(--red);color:var(--white)}
.stat.red b{color:var(--white)}

.kpi{position:absolute;text-align:center;font-size:1.9px;color:#444;line-height:2.6px}
.kpi b{display:block;font-size:2.8px;color:var(--red);font-weight:600}
.kpi.box{background:var(--red);color:var(--white);padding:1.8px 4px}
.kpi.box b{color:var(--white)}

/* swot */
.swot{position:absolute;top:42px;bottom:5px;width:40px;padding:2px 3px}
.swot .h{font-size:2.2px}
.swot.red{background:var(--red)}
.swot.blue{background:var(--blue)}
.swot.red .h,.swot.blue .h,.swot.red .p,.swot.blue .p{color:var(--white)}

/* leaders / team */
.avatar{position:absolute;border-radius:50%;background:linear-gradient(160deg,#b9a48e,#6d5a4c);border:.8px solid var(--white)}
.name{position:absolute;text-align:center;font-size:1.8px;line-height:2.3px;color:var(--blue);font-weight:600}
.name span{display:block;color:#555;font-weight:400}

/* infographic 03 */
.slide.redbg{background:var(--red)}
.slide.bluebg{background:var(--blue)}
.icard{position:absolute;top:35px;width:31px;height:48px;background:var(--blue);border-radius:0 8px 0 8px;padding:12px 2.5px 0}
.icard .p{color:var(--white)}
.icard .h{color:var(--white);font-size:2px}
.inum{position:absolute;top:-6px;left:4px;width:22px;height:22px;border-radius:50%;background:var(--blue);border:1.2px solid var(--white);color:var(--white);text-align:center;font-weight:600;font-size:5.4px;line-height:13px}
.inum span{display:block;font-size:1.5px;line-height:1px;font-weight:400}

/* agenda */
.acard{position:absolute;top:27px;width:42px;height:49px;background:#f3f3f4;box-shadow:.5px 1px 2px rgba(0,0,0,.2);padding:15px 3px 0;text-align:center}
.acard .h{font-size:2.3px}
.acard.red{background:var(--red)}
.acard.red .h,.acard.red .p{color:var(--white)}

/* table */
.tbl{position:absolute;left:26px;top:28px;width:125px;border-collapse:collapse;font-size:1.7px;color:var(--white)}
.tbl th{background:#155789;font-weight:600;text-align:left;padding:1px 1.5px}
.tbl td{padding:1px 1.5px;height:5.4px}
.tbl tr.dark td{background:#1c5f96}

/* thank you */
.thanks{position:absolute;left:0;right:0;top:30px;text-align:center;font-size:9.5px;font-weight:300;color:var(--white)}
.thanks-p{position:absolute;left:28px;right:28px;top:44px;text-align:center;font-size:1.9px;line-height:2.5px;color:var(--white)}

.dash-stat{position:absolute;text-align:center;font-size:1.8px;color:#444;line-height:2.6px}
.dash-stat b{display:block;color:var(--blue);font-weight:600;font-size:2.2px}
.dash-stat.box{background:var(--blue);color:var(--white);padding:1px 5px}
.dash-stat.box b{color:var(--white)}
</style>
</head>
<body>

<!-- 1 Cover -->
<section class="slide c1 r1">
  <div class="cover-top"><div class="cover-brand">VeroTide</div></div>
  <div class="cover-band" role="img" aria-label="Photo of hands working on a tablet, tinted blue"></div>
  <div class="cover-title">PRESENTATION TITLE</div>
  <div class="cover-sub">SUBTITLE</div>
  <div class="cover-date">JANUARY 2023</div>
  <div class="cover-web">www.verotide.example</div>
</section>

<!-- 2 Contents -->
<section class="slide c2 r1">
  <div class="title" style="top:7px">Contents</div>
  <div class="toc" style="left:28px;top:24px"><span>Cover Slide</span><b>01</b></div>
  <div class="toc" style="left:28px;top:36px"><span>Contents</span><b>03</b></div>
  <div class="toc" style="left:28px;top:49px"><span>About Us</span><b>04</b></div>
  <div class="toc" style="left:28px;top:62px"><span>Our Mission</span><b>05</b></div>
  <div class="toc" style="left:28px;top:76px"><span>Our Vision</span><b>07</b></div>
  <div class="toc" style="left:100px;top:24px"><span>Infographic 1</span><b>01</b></div>
  <div class="toc" style="left:100px;top:36px"><span>Planning</span><b>03</b></div>
  <div class="toc" style="left:100px;top:49px"><span>Company info</span><b>04</b></div>
  <div class="toc" style="left:100px;top:62px"><span>Our Team</span><b>06</b></div>
  <div class="toc" style="left:100px;top:76px"><span>Dashboard</span><b>07</b></div>
  <div class="footbar"></div><div class="brand">VeroTide</div><div class="page">PAGE | 02</div>
</section>

<!-- 3 Vision -->
<section class="slide c3 r1">
  <div class="title" style="top:7px">Our Vision</div>
  <div class="red-band">We connect homes and businesses with fast, stable broadband and managed network services, built around clear pricing, local engineers and support that answers quickly every day of the year.</div>
  <div class="footbar"></div><div class="brand">VeroTide</div><div class="page">PAGE | 03</div>
</section>

<!-- 4 Mission -->
<section class="slide c4 r1">
  <div class="title" style="top:7px">Our Mission</div>
  <div class="mblock shade" style="left:12px;top:25px"><div class="h">Mission 1</div><div class="p">Reliable links for every site, backed by clear service levels.</div></div>
  <div class="mblock" style="left:66px;top:25px"><div class="h">Mission 1</div><div class="p">Reliable links for every site, backed by clear service levels.</div></div>
  <div class="mblock" style="left:120px;top:25px"><div class="h">Mission 1</div><div class="p">Reliable links for every site, backed by clear service levels.</div></div>
  <div class="mblock" style="left:12px;top:53px"><div class="h">Mission 1</div><div class="p">Secure networks, steady support and honest advice.</div></div>
  <div class="mblock" style="left:66px;top:53px"><div class="h">Mission 1</div><div class="p">Secure networks, steady support and honest advice.</div></div>
  <div class="mblock shade" style="left:120px;top:53px"><div class="h">Mission 1</div><div class="p">Secure networks, steady support and honest advice.</div></div>
  <div class="footbar"></div><div class="brand">VeroTide</div><div class="page">PAGE | 04</div>
</section>

<!-- 5 Achievements -->
<section class="slide c5 r1">
  <div class="photo" style="left:0;top:0;width:67px;height:94px;background:linear-gradient(150deg,#6f7c86,#c9c3bc 55%,#8a8f96)" role="img" aria-label="Photo of two colleagues working together at a laptop"></div>
  <div class="title left" style="left:73px;top:22px">Our Acheivements</div>
  <div class="abs p" style="left:73px;top:33px;width:96px">Years of steady growth across broadband and network services, with teams trusted by businesses in every region we serve.</div>
  <div class="stat" style="left:73px;top:50px"><b>15</b>Companies</div>
  <div class="stat" style="left:99px;top:50px"><b>1,000</b>Clients</div>
  <div class="stat red" style="left:125px;top:50px"><b>46</b>Employees</div>
  <div class="footbar"></div><div class="brand">VeroTide</div><div class="page">PAGE | 05</div>
</section>

<!-- 6 Services -->
<section class="slide c1 r2">
  <div class="title" style="top:7px">Services</div>
  <div class="sub" style="top:16px">Broadband, networking and support, planned around your business.</div>
  <div class="photo" style="left:9px;top:26px;width:44px;height:37px;background:linear-gradient(150deg,#d8c9ae,#5d6b3c)" role="img" aria-label="Photo of hands preparing a dish"></div>
  <div class="photo" style="left:66px;top:26px;width:44px;height:37px;background:linear-gradient(150deg,#8a7b6d,#3d3a38)" role="img" aria-label="Photo of a team meeting around a table"></div>
  <div class="photo" style="left:122px;top:26px;width:44px;height:37px;background:linear-gradient(150deg,#e8ebee,#7e8e9c)" role="img" aria-label="Photo of two colleagues in an office"></div>
  <div class="abs center" style="left:9px;top:66px;width:44px"><div class="h" style="font-size:2.2px">Service 1</div><div class="p">Fibre broadband with steady speeds and fair plans.</div></div>
  <div class="abs center" style="left:66px;top:66px;width:44px"><div class="h" style="font-size:2.2px">Service 2</div><div class="p">Managed networks, monitored around the clock.</div></div>
  <div class="abs center" style="left:122px;top:66px;width:44px"><div class="h" style="font-size:2.2px">Service 3</div><div class="p">On-site engineers for installs and quick repairs.</div></div>
  <div class="footbar"></div><div class="brand">VeroTide</div><div class="page">PAGE | 06</div>
</section>

<!-- 7 Our Company -->
<section class="slide c2 r2">
  <div class="title" style="top:7px">Our Company</div>
  <div class="sub" style="top:16px">A group of two specialist companies in network services.</div>
  <div class="abs p center" style="left:20px;top:29px;width:136px">VeroTide brings together k7gridworks and Quiet Harbor to deliver broadband, connectivity and network management for offices, shops and homes. Our engineers design, install and maintain each link, while our support desk keeps every customer online, informed and in control of costs, speed and security across all of their sites.</div>
  <div class="kpi" style="left:10px;top:70px;width:26px"><b>2100</b>Evaluations</div>
  <div class="kpi" style="left:44px;top:70px;width:36px"><b>3100</b>Production profitably</div>
  <div class="kpi box" style="left:101px;top:68px;width:26px"><b>2100</b>Companies</div>
  <div class="kpi" style="left:138px;top:70px;width:28px"><b>14</b>Certifications</div>
  <div class="footbar"></div><div class="brand">VeroTide</div><div class="page">PAGE | 07</div>
</section>

<!-- 8 Analysis Chart -->
<section class="slide c3 r2">
  <div class="title" style="top:7px">Analysis Chart</div>
  <div class="abs h" style="left:9px;top:27px;font-size:2.2px">Bar Chart</div>
  <svg style="left:8px;top:36px" width="80" height="40" viewBox="0 0 80 40">
    <g stroke="#ddd" stroke-width=".3"><line x1="10" y1="0" x2="10" y2="33"/><line x1="30" y1="0" x2="30" y2="33"/><line x1="50" y1="0" x2="50" y2="33"/><line x1="70" y1="0" x2="70" y2="33"/></g>
    <g font-size="1.6" fill="#777"><text x="0" y="4">Cat 1</text><text x="0" y="12">Cat 2</text><text x="0" y="20">Cat 3</text><text x="0" y="28">Cat 4</text></g>
    <rect x="10" y="2" width="18" height="2.6" fill="#1fa3de"/><rect x="28" y="2" width="12" height="2.6" fill="#1b5f9a"/><rect x="40" y="2" width="22" height="2.6" fill="#8a8a8a"/>
    <rect x="10" y="10" width="22" height="2.6" fill="#1fa3de"/><rect x="32" y="10" width="8" height="2.6" fill="#1b5f9a"/><rect x="40" y="10" width="10" height="2.6" fill="#8a8a8a"/>
    <rect x="10" y="18" width="14" height="2.6" fill="#1fa3de"/><rect x="24" y="18" width="14" height="2.6" fill="#1b5f9a"/><rect x="38" y="18" width="18" height="2.6" fill="#8a8a8a"/>
    <rect x="10" y="26" width="20" height="2.6" fill="#1fa3de"/><rect x="30" y="26" width="10" height="2.6" fill="#1b5f9a"/><rect x="40" y="26" width="16" height="2.6" fill="#8a8a8a"/>
  </svg>
  <div class="abs" style="left:94px;top:26px;width:74px"><div class="h" style="font-size:2.1px">Analysis 1</div><div class="p">Uptime rose across all regions this year, with fewer faults and faster repair times for business lines.</div></div>
  <div class="abs" style="left:94px;top:45px;width:74px"><div class="h" style="font-size:2.1px">Analysis 2</div><div class="p">New fibre areas added steady demand, mostly from small offices moving off older copper links.</div></div>
  <div class="abs" style="left:94px;top:64px;width:74px"><div class="h" style="font-size:2.1px">Analysis 3</div><div class="p">Support calls dropped while customer scores improved after the new monitoring tools went live.</div></div>
  <div class="footbar"></div><div class="brand">VeroTide</div><div class="page">PAGE | 08</div>
</section>

<!-- 9 SWOT -->
<section class="slide c4 r2">
  <div class="title" style="top:7px;color:var(--red)">S.W.O.T Analysis</div>
  <div class="abs p center" style="left:30px;top:20px;width:116px">A short look at where the group stands today and where the network business can grow next.</div>
  <div class="swot" style="left:7px"><div class="h">Strength</div><div class="p">1. Local engineers<br>2. Fast fibre network<br>3. Strong support desk<br>4. Fair pricing</div></div>
  <div class="swot red" style="left:47px"><div class="h">Weakness</div><div class="p">1. Limited rural reach<br>2. Small sales team<br>3. Older billing tools<br>4. Slow brand growth</div></div>
  <div class="swot" style="left:87px"><div class="h">Opportunity</div><div class="p">1. New fibre areas<br>2. Remote work demand<br>3. Managed security<br>4. Partner resale</div></div>
  <div class="swot blue" style="left:128px"><div class="h">Threat</div><div class="p">1. Larger rivals<br>2. Rising costs<br>3. Price cuts<br>4. Supply delays</div></div>
  <div class="footbar"></div><div class="brand">VeroTide</div><div class="page">PAGE | 09</div>
</section>

<!-- 10 Process -->
<section class="slide c5 r2">
  <div class="photo" style="left:0;top:0;width:70px;height:76px;background:linear-gradient(150deg,#3c4a58,#8d7a68 60%,#2e3944)" role="img" aria-label="Photo of a young man working on a laptop"></div>
  <div class="title left" style="left:87px;top:22px">Process</div>
  <div class="abs p" style="left:87px;top:33px;width:82px">From first call to live service, every project follows three clear steps.</div>
  <svg style="left:70px;top:40px" width="20" height="40" viewBox="0 0 20 40"><g stroke="#1fa3de" stroke-width=".4" fill="none"><path d="M0 3 H16"/><path d="M0 12 H28"/><path d="M0 22 H34"/></g></svg>
  <div class="abs" style="left:87px;top:41px;width:82px"><div class="h" style="font-size:2.1px">Step 1</div><div class="p">Survey the site and agree needs.</div></div>
  <div class="abs" style="left:99px;top:51px;width:70px"><div class="h" style="font-size:2.1px">Step 2</div><div class="p">Install and test every link.</div></div>
  <div class="abs" style="left:105px;top:61px;width:64px"><div class="h" style="font-size:2.1px">Step 3</div><div class="p">Monitor, support and improve.</div></div>
  <div class="footbar"></div><div class="brand">VeroTide</div><div class="page">PAGE | 10</div>
</section>

<!-- 11 Planning -->
<section class="slide c1 r3">
  <div class="photo" style="left:8px;top:22px;width:81px;height:69px;background:linear-gradient(170deg,#b8d6ea,#e9e7e2 45%,#b9876c 70%,#2ea0b8)" role="img" aria-label="Photo of a modern house with a pool"></div>
  <div class="title left" style="left:95px;top:20px">Planning</div>
  <div class="abs p" style="left:95px;top:31px;width:75px">Each rollout is planned with clear dates, costs and owners so customers know what happens next.</div>
  <div class="abs" style="left:95px;top:42px;width:75px"><div class="h" style="font-size:2.1px">Network design</div><div class="p">Map sites, loads and routes.<br>Choose the right fibre plan.<br>Agree timings with your team.</div></div>
  <div class="abs" style="left:95px;top:59px;width:75px"><div class="h" style="font-size:2.1px">Go-live support</div><div class="p">Test each connection on site.<br>Hand over clear documents.<br>Stay on call for the first weeks.</div></div>
  <div class="footbar"></div><div class="brand">VeroTide</div><div class="page">PAGE | 11</div>
</section>

<!-- 12 Images -->
<section class="slide c2 r3">
  <div class="photo" style="left:9px;top:16px;width:38px;height:32px;background:linear-gradient(150deg,#2a2420,#c89a5a 60%,#3a2e26)" role="img" aria-label="Photo of sparks from metal work"></div>
  <div class="photo" style="left:84px;top:16px;width:38px;height:32px;background:linear-gradient(150deg,#d9d3cc,#6a5a4e)" role="img" aria-label="Photo of a woman working at a desk"></div>
  <div class="photo" style="left:47px;top:47px;width:37px;height:39px;background:linear-gradient(150deg,#3d4c66,#c9cdd6 60%,#53627a)" role="img" aria-label="Photo of hands holding a small house model"></div>
  <div class="abs" style="left:50px;top:19px;width:32px"><div class="h" style="font-size:2.1px">Item 2</div><div class="p">Short note on this image and why it matters.</div></div>
  <div class="abs" style="left:9px;top:54px;width:36px"><div class="h" style="font-size:2.1px">Item 1</div><div class="p">Short note on this image and why it matters.</div></div>
  <div class="abs" style="left:88px;top:54px;width:34px"><div class="h" style="font-size:2.1px">Item 3</div><div class="p">Short note on this image and why it matters.</div></div>
  <div class="title left" style="left:127px;top:24px">Images</div>
  <div class="abs p" style="left:127px;top:35px;width:43px">Use this page to show real sites, teams and installs from recent projects.</div>
  <div class="footbar"></div><div class="brand">VeroTide</div><div class="page">PAGE | 12</div>
</section>

<!-- 13 Our Leaders -->
<section class="slide c3 r3">
  <div class="title" style="top:7px">Our Leaders</div>
  <div class="sub" style="top:16px">The people guiding our group and its companies.</div>
  <div class="abs" style="left:0;right:0;top:23px;height:19px;background:var(--red)"></div>
  <div class="avatar" role="img" aria-label="Portrait photo of a team leader" style="left:16px;top:30px;width:20px;height:20px"></div>
  <div class="avatar" role="img" aria-label="Portrait photo of a team leader" style="left:58px;top:30px;width:20px;height:20px"></div>
  <div class="avatar" role="img" aria-label="Portrait photo of a team leader" style="left:101px;top:30px;width:20px;height:20px"></div>
  <div class="avatar" role="img" aria-label="Portrait photo of a team leader" style="left:140px;top:30px;width:20px;height:20px"></div>
  <div class="name" style="left:8px;top:52px;width:36px">Ryan Calder<span>Manager</span></div>
  <div class="name" style="left:50px;top:52px;width:36px">Ryan Calder<span>Manager</span></div>
  <div class="name" style="left:93px;top:52px;width:36px">Ryan Calder<span>Manager</span></div>
  <div class="name" style="left:132px;top:52px;width:36px">Ryan Calder<span>Manager</span></div>
  <div class="abs p center" style="left:8px;top:58px;width:36px">Leads sales and customer growth across all regions.</div>
  <div class="abs p center" style="left:50px;top:58px;width:36px">Leads sales and customer growth across all regions.</div>
  <div class="abs p center" style="left:93px;top:58px;width:36px">Leads sales and customer growth across all regions.</div>
  <div class="abs p center" style="left:132px;top:58px;width:36px">Leads sales and customer growth across all regions.</div>
  <div class="footbar"></div><div class="brand">VeroTide</div><div class="page">PAGE | 13</div>
</section>

<!-- 14 Our Team -->
<section class="slide c4 r3">
  <div class="title" style="top:7px">Our Team</div>
  <div class="sub" style="top:16px">The engineers and advisers behind every connection.</div>
  <div class="abs" style="left:140px;top:19px;width:36px;height:38px;background:var(--red);border-radius:6px 0 0 6px"></div>
  <div class="avatar" role="img" aria-label="Portrait photo of a team member" style="left:20px;top:25px;width:17px;height:17px"></div>
  <div class="avatar" role="img" aria-label="Portrait photo of a team member" style="left:62px;top:25px;width:17px;height:17px"></div>
  <div class="avatar" role="img" aria-label="Portrait photo of a team member" style="left:104px;top:25px;width:17px;height:17px"></div>
  <div class="avatar" role="img" aria-label="Portrait photo of a team member" style="left:149px;top:24px;width:18px;height:18px"></div>
  <div class="name" style="left:11px;top:45px;width:36px">Ryan Calder<span>Manager</span></div>
  <div class="name" style="left:53px;top:45px;width:36px">Ryan Calder<span>Manager</span></div>
  <div class="name" style="left:95px;top:45px;width:36px">Ryan Calder<span>Manager</span></div>
  <div class="name" style="left:140px;top:45px;width:36px;color:var(--white)">Ryan Calder<span style="color:var(--white)">Manager</span></div>
  <div class="avatar" role="img" aria-label="Portrait photo of a team member" style="left:20px;top:61px;width:17px;height:17px"></div>
  <div class="avatar" role="img" aria-label="Portrait photo of a team member" style="left:62px;top:61px;width:17px;height:17px"></div>
  <div class="avatar" role="img" aria-label="Portrait photo of a team member" style="left:104px;top:61px;width:17px;height:17px"></div>
  <div class="avatar" role="img" aria-label="Portrait photo of a team member" style="left:149px;top:61px;width:17px;height:17px"></div>
  <div class="name" style="left:11px;top:81px;width:36px">Ryan Calder<span>Manager</span></div>
  <div class="name" style="left:53px;top:81px;width:36px">Ryan Calder<span>Manager</span></div>
  <div class="name" style="left:95px;top:81px;width:36px">Ryan Calder<span>Manager</span></div>
  <div class="name" style="left:140px;top:81px;width:36px">Ryan Calder<span>Manager</span></div>
  <div class="footbar"></div><div class="brand">VeroTide</div><div class="page">PAGE | 14</div>
</section>

<!-- 15 Timeline -->
<section class="slide c5 r3">
  <div class="title" style="top:7px">Timeline</div>
  <svg style="left:0;top:0" width="176" height="99" viewBox="0 0 176 99">
    <line x1="14" y1="50" x2="162" y2="50" stroke="#999" stroke-width=".3" stroke-dasharray="1 .8"/>
    <circle cx="14" cy="50" r=".8" fill="#999"/><circle cx="162" cy="50" r=".8" fill="#999"/>
    <g font-size="1.4" fill="#fff" text-anchor="middle" font-weight="600">
      <circle cx="27" cy="50" r="3.2" fill="#1fa3de"/><text x="27" y="50.5">2020</text>
      <circle cx="49" cy="50" r="3.2" fill="#d8222a"/><text x="49" y="50.5">2021</text>
      <circle cx="72" cy="50" r="3.2" fill="#1fa3de"/><text x="72" y="50.5">2022</text>
      <circle cx="94" cy="50" r="3.2" fill="#d8222a"/><text x="94" y="50.5">2023</text>
      <circle cx="117" cy="50" r="3.2" fill="#1fa3de"/><text x="117" y="50.5">2024</text>
      <circle cx="139" cy="50" r="3.2" fill="#d8222a"/><text x="139" y="50.5">2025</text>
    </g>
    <g fill="none" stroke-width=".4"><circle cx="49" cy="22" r="1.5" stroke="#d8222a"/><circle cx="94" cy="22" r="1.5" stroke="#d8222a"/><circle cx="139" cy="22" r="1.5" stroke="#d8222a"/>
    <circle cx="27" cy="68" r="1.5" stroke="#1fa3de"/><circle cx="72" cy="68" r="1.5" stroke="#1fa3de"/><circle cx="117" cy="68" r="1.5" stroke="#1fa3de"/></g>
  </svg>
  <div class="abs center" style="left:33px;top:25px;width:32px"><div class="h" style="font-size:2.1px;color:var(--red)">Item 1</div><div class="p">First fibre routes opened to business parks.</div></div>
  <div class="abs center" style="left:78px;top:25px;width:32px"><div class="h" style="font-size:2.1px;color:var(--red)">Item 1</div><div class="p">First fibre routes opened to business parks.</div></div>
  <div class="abs center" style="left:123px;top:25px;width:32px"><div class="h" style="font-size:2.1px;color:var(--red)">Item 1</div><div class="p">First fibre routes opened to business parks.</div></div>
  <div class="abs center" style="left:11px;top:71px;width:32px"><div class="h" style="font-size:2.1px">Item 1</div><div class="p">Managed network service added for clients.</div></div>
  <div class="abs center" style="left:56px;top:71px;width:32px"><div class="h" style="font-size:2.1px">Item 1</div><div class="p">Managed network service added for clients.</div></div>
  <div class="abs center" style="left:101px;top:71px;width:32px"><div class="h" style="font-size:2.1px">Item 1</div><div class="p">Managed network service added for clients.</div></div>
  <div class="footbar"></div><div class="brand">VeroTide</div><div class="page">PAGE | 15</div>
</section>

<!-- 16 Doughnut Chart -->
<section class="slide c1 r4">
  <div class="title left" style="left:8px;top:22px">Doughnut Chart</div>
  <div class="abs p" style="left:8px;top:67px;width:38px">Quarterly share of new connections across the group, split by quarter.</div>
  <svg style="left:63px;top:27px" width="50" height="50" viewBox="0 0 50 50">
    <g fill="none" stroke-width="7" transform="rotate(-90 25 25)">
      <circle cx="25" cy="25" r="20" stroke="#1fa3de" stroke-dasharray="75.4 125.7"/>
      <circle cx="25" cy="25" r="20" stroke="#1b5f9a" stroke-dasharray="30 125.7" stroke-dashoffset="-75.4"/>
      <circle cx="25" cy="25" r="20" stroke="#8a8a8a" stroke-dasharray="10 125.7" stroke-dashoffset="-105.4"/>
      <circle cx="25" cy="25" r="20" stroke="#cfcfcf" stroke-dasharray="10.3 125.7" stroke-dashoffset="-115.4"/>
    </g>
  </svg>
  <div class="abs" style="left:64px;top:79px;font-size:1.5px;color:#777">● 1st Qtr  ● 2nd Qtr  ● 3rd Qtr  ● 4th Qtr</div>
  <div class="abs h" style="left:127px;top:68px;font-size:3.2px;line-height:4.3px">Total<br>13559</div>
  <div class="footbar"></div><div class="brand">VeroTide</div><div class="page">PAGE | 16</div>
</section>

<!-- 17 Infographic 01 -->
<section class="slide c2 r4">
  <div class="title" style="top:7px">infographic 01</div>
  <svg style="left:0;top:0" width="176" height="99" viewBox="0 0 176 99">
    <g stroke="#ccc" stroke-width=".3"><line x1="32" y1="40" x2="46" y2="40"/><line x1="65" y1="40" x2="79" y2="40"/><line x1="97" y1="40" x2="111" y2="40"/><line x1="130" y1="40" x2="144" y2="40"/></g>
    <g fill="#f3f3f4" stroke="#e1e1e1" stroke-width=".3">
      <polygon points="23,31 31,35.5 31,44.5 23,49 15,44.5 15,35.5"/>
      <polygon points="56,31 64,35.5 64,44.5 56,49 48,44.5 48,35.5"/>
      <polygon points="121,31 129,35.5 129,44.5 121,49 113,44.5 113,35.5"/>
      <polygon points="154,31 162,35.5 162,44.5 154,49 146,44.5 146,35.5"/>
    </g>
    <polygon points="88,31 96,35.5 96,44.5 88,49 80,44.5 80,35.5" fill="#1fa3de"/>
    <g font-size="1.6" text-anchor="middle" fill="#1fa3de" font-weight="600"><text x="23" y="40.5">Lorem ipsum</text><text x="56" y="40.5">Lorem ipsum</text><text x="88" y="40.5" fill="#fff">Lorem ipsum</text><text x="121" y="40.5">Lorem ipsum</text><text x="154" y="40.5">Lorem ipsum</text></g>
  </svg>
  <div class="abs center" style="left:10px;top:56px;width:26px"><div class="h" style="font-size:1.9px">Lorem ipsum</div><div class="p">Plan the link and agree the budget early.</div></div>
  <div class="abs center" style="left:43px;top:56px;width:26px"><div class="h" style="font-size:1.9px">Lorem ipsum</div><div class="p">Plan the link and agree the budget early.</div></div>
  <div class="abs center" style="left:75px;top:56px;width:26px"><div class="h" style="font-size:1.9px">Lorem ipsum</div><div class="p">Plan the link and agree the budget early.</div></div>
  <div class="abs center" style="left:108px;top:56px;width:26px"><div class="h" style="font-size:1.9px">Lorem ipsum</div><div class="p">Plan the link and agree the budget early.</div></div>
  <div class="abs center" style="left:141px;top:56px;width:26px"><div class="h" style="font-size:1.9px">Lorem ipsum</div><div class="p">Plan the link and agree the budget early.</div></div>
  <div class="footbar"></div><div class="brand">VeroTide</div><div class="page">PAGE | 17</div>
</section>

<!-- 18 Infographic 02 -->
<section class="slide c3 r4">
  <div class="title" style="top:7px">infographic 02</div>
  <svg style="left:0;top:0" width="176" height="99" viewBox="0 0 176 99">
    <defs><linearGradient id="pill" x1="0" y1="0" x2="0" y2="1"><stop offset="0" stop-color="#1fa3de"/><stop offset="1" stop-color="#1b5f9a"/></linearGradient></defs>
    <g fill="url(#pill)"><rect x="26" y="26" width="12" height="24" rx="6"/><rect x="63" y="26" width="12" height="24" rx="6"/><rect x="100" y="26" width="12" height="24" rx="6"/><rect x="137" y="26" width="12" height="24" rx="6"/></g>
    <g font-size="1.6" fill="#fff" text-anchor="middle" font-weight="600"><text x="32" y="37">Lorem</text><text x="32" y="39.2">Ipsum</text><text x="69" y="37">Lorem</text><text x="69" y="39.2">Ipsum</text><text x="106" y="37">Lorem</text><text x="106" y="39.2">Ipsum</text><text x="143" y="37">Lorem</text><text x="143" y="39.2">Ipsum</text></g>
    <g><polygon points="32,68 37,71 37,77 32,80 27,77 27,71" fill="#1fa3de"/><polygon points="69,68 74,71 74,77 69,80 64,77 64,71" fill="#1b5f9a"/><polygon points="106,68 111,71 111,77 106,80 101,77 101,71" fill="#1fa3de"/><polygon points="143,68 148,71 148,77 143,80 138,77 138,71" fill="#1b5f9a"/></g>
    <g fill="none" stroke="#fff" stroke-width=".4"><rect x="30.3" y="72.3" width="3.4" height="3.4"/><rect x="67.5" y="71.8" width="3" height="4.4"/><path d="M104.3 72 h3.4 v4 h-3.4z M105 73.5 h2"/><path d="M143 71.8 l2 .8 v1.6 c0 1.4 -1 2.2 -2 2.6 c-1 -.4 -2 -1.2 -2 -2.6 v-1.6z"/></g>
  </svg>
  <div class="abs p center" style="left:18px;top:55px;width:28px">Fast setup with clear steps for every site.</div>
  <div class="abs p center" style="left:55px;top:55px;width:28px">Fast setup with clear steps for every site.</div>
  <div class="abs p center" style="left:92px;top:55px;width:28px">Fast setup with clear steps for every site.</div>
  <div class="abs p center" style="left:129px;top:55px;width:28px">Fast setup with clear steps for every site.</div>
  <div class="footbar"></div><div class="brand">VeroTide</div><div class="page">PAGE | 18</div>
</section>

<!-- 19 Infographic 03 -->
<section class="slide c4 r4 redbg">
  <div class="title" style="top:7px;color:var(--white)">infographic 03</div>
  <div class="icard" style="left:8px"><div class="inum">500<span>Point A</span></div><div class="h">Step One</div><div class="p">Survey each site and record what the team needs from the network.</div></div>
  <div class="icard" style="left:50px"><div class="inum">600<span>Point B</span></div><div class="h">Step Two</div><div class="p">Design the links, choose hardware and agree a clear timeline.</div></div>
  <div class="icard" style="left:92px"><div class="inum">700<span>Point C</span></div><div class="h">Step Three</div><div class="p">Install, test and hand over with full notes for your staff.</div></div>
  <div class="icard" style="left:134px"><div class="inum">800<span>Point D</span></div><div class="h">Step Four</div><div class="p">Monitor daily and fix issues before they slow you down.</div></div>
  <div class="footbar"></div><div class="brand">VeroTide</div><div class="page">PAGE | 19</div>
</section>

<!-- 20 Project Agenda -->
<section class="slide c5 r4">
  <div class="title" style="top:7px">Project Agenda</div>
  <div class="sub" style="top:16px">Key dates for the next stage of the rollout.</div>
  <div class="acard" style="left:18px"><div class="h">23<sup>rd</sup> June</div><div class="p">Site surveys complete across the first group of offices.</div></div>
  <div class="acard red" style="left:67px"><div class="h">14<sup>th</sup> July</div><div class="p">New fibre links live for all partner sites.</div></div>
  <div class="acard" style="left:117px"><div class="h">01<sup>st</sup> December</div><div class="p">Full review and plan for next year's growth.</div></div>
  <svg style="left:0;top:0" width="176" height="99" viewBox="0 0 176 99">
    <g fill="none" stroke="#1fa3de" stroke-width=".4"><circle cx="39" cy="35" r="2"/><path d="M38.2 37.5 h1.6"/></g>
    <g fill="none" stroke="#fff" stroke-width=".4"><rect x="86" y="33" width="5" height="3.5" rx=".5"/><path d="M87.5 36.5 l-.5 1.5 1.5 -1.5"/></g>
    <g fill="#1fa3de"><circle cx="136" cy="33.5" r="1"/><circle cx="139" cy="33.5" r="1"/><rect x="134.8" y="35" width="2.4" height="2" rx=".6"/><rect x="137.8" y="35" width="2.4" height="2" rx=".6"/></g>
  </svg>
  <div class="footbar"></div><div class="brand">VeroTide</div><div class="page">PAGE | 20</div>
</section>

<!-- 21 Monthly Chart -->
<section class="slide c1 r5">
  <div class="title" style="top:7px">Monthly Chart</div>
  <div class="sub" style="top:16px">Monthly growth in active business lines.</div>
  <svg style="left:8px;top:26px" width="120" height="52" viewBox="0 0 120 52">
    <g stroke="#e1e1e1" stroke-width=".3"><line x1="6" y1="2" x2="118" y2="2"/><line x1="6" y1="10" x2="118" y2="10"/><line x1="6" y1="18" x2="118" y2="18"/><line x1="6" y1="26" x2="118" y2="26"/><line x1="6" y1="34" x2="118" y2="34"/><line x1="6" y1="42" x2="118" y2="42"/></g>
    <g font-size="1.5" fill="#888"><text x="2" y="2.5">6</text><text x="2" y="10.5">5</text><text x="2" y="18.5">4</text><text x="2" y="26.5">3</text><text x="2" y="34.5">2</text><text x="2" y="42.5">1</text>
    <text x="15" y="46">Jan</text><text x="33" y="46">Feb</text><text x="51" y="46">Mar</text><text x="69" y="46">Apr</text><text x="87" y="46">May</text><text x="105" y="46">Jun</text></g>
    <polyline points="16,19 34,26 52,21 70,17 88,23 106,8" fill="none" stroke="#1fa3de" stroke-width=".7"/>
  </svg>
  <div class="abs h" style="left:131px;top:27px;font-size:2.1px">May</div>
  <div class="abs" style="left:131px;top:31px;width:8px;height:8px;border-radius:50%;background:var(--blue);color:#fff;font-size:1.8px;font-weight:600;text-align:center;line-height:8px">3.5</div>
  <div class="abs p" style="left:131px;top:41px;width:38px">Steady month with strong renewals from small offices.</div>
  <div class="abs h" style="left:131px;top:51px;font-size:2.1px;color:var(--red)">June</div>
  <div class="abs" style="left:131px;top:55px;width:8px;height:8px;border-radius:50%;background:var(--red);color:#fff;font-size:1.8px;font-weight:600;text-align:center;line-height:8px">5.7</div>
  <div class="abs p" style="left:131px;top:65px;width:38px">Record month after new fibre areas went live.</div>
  <div class="footbar"></div><div class="brand">VeroTide</div><div class="page">PAGE | 21</div>
</section>

<!-- 22 Three Point Value -->
<section class="slide c2 r5">
  <div class="title" style="top:7px">Three Point Value</div>
  <div class="sub" style="top:16px">What customers value most about our service.</div>
  <svg style="left:0;top:0" width="176" height="99" viewBox="0 0 176 99">
    <polyline points="17,51 41,66 64,40" fill="none" stroke="#8a8a8a" stroke-width="3.4" stroke-linejoin="round"/>
    <g fill="#1fa3de" stroke="#fff" stroke-width=".8"><circle cx="17" cy="51" r="5.5"/><circle cx="41" cy="66" r="5.5"/><circle cx="64" cy="40" r="5.5"/></g>
    <g fill="#fff" font-size="3.2" font-weight="600" text-anchor="middle"><text x="17" y="52.2">1.</text><text x="41" y="67.2">2.</text><text x="64" y="41.2">3.</text></g>
  </svg>
  <div class="abs" style="left:88px;top:36px;width:78px"><div class="h" style="font-size:2.4px">56%</div><div class="p">Say fast local support is the main reason they stay with us.</div></div>
  <div class="abs" style="left:88px;top:50px;width:78px"><div class="h" style="font-size:2.4px">70%</div><div class="p">Rate our network speed above their previous provider's.</div></div>
  <div class="abs" style="left:88px;top:64px;width:78px"><div class="h" style="font-size:2.4px">81%</div><div class="p">Would recommend our group to another business owner.</div></div>
  <div class="footbar"></div><div class="brand">VeroTide</div><div class="page">PAGE | 22</div>
</section>

<!-- 23 Table -->
<section class="slide c3 r5 bluebg">
  <div class="title" style="top:7px;color:var(--white)">Table</div>
  <div class="sub" style="top:16px;color:var(--white)">Service packages and current sales figures.</div>
  <table class="tbl">
    <tr><th>Data Name</th><th>Product</th><th>Profit</th><th>Optional</th><th>Sold</th><th>Performance</th></tr>
    <tr><td>Data 1</td><td>Product Name</td><td>$900,000.00</td><td>Yes</td><td>70</td><td>45%</td></tr>
    <tr class="dark"><td>Data 2</td><td>Product Name</td><td>$900,000.00</td><td>No</td><td>30</td><td>20%</td></tr>
    <tr><td>Data 3</td><td>Product Name</td><td>$900,000.00</td><td>No</td><td>20</td><td>15%</td></tr>
    <tr class="dark"><td>Data 4</td><td>Product Name</td><td>$900,000.00</td><td>Yes</td><td>100</td><td>60%</td></tr>
    <tr><td>Data 5</td><td>Product Name</td><td>$900,000.00</td><td>Yes</td><td>50</td><td>40%</td></tr>
  </table>
  <div class="brand">VeroTide</div><div class="page">PAGE | 23</div>
</section>

<!-- 24 Dashboard 01 -->
<section class="slide c4 r5">
  <div class="title" style="top:7px">Dashboard 01</div>
  <div class="dash-stat" style="left:10px;top:28px;width:24px">Customers<b>2100</b></div>
  <div class="dash-stat" style="left:54px;top:28px;width:24px">Profitably<b>3100</b></div>
  <div class="dash-stat box" style="left:100px;top:26px;width:26px">Projects<b>300</b></div>
  <div class="dash-stat" style="left:142px;top:28px;width:20px">Returns<b>14</b></div>
  <div class="dash-stat" style="left:8px;top:44px;width:28px"><b style="font-size:1.8px">6 Active Users</b>last 10 Days</div>
  <div class="dash-stat" style="left:52px;top:44px;width:28px"><b style="font-size:1.8px">2 Users per role</b>last 10 Days</div>
  <svg style="left:0;top:0" width="176" height="99" viewBox="0 0 176 99">
    <g><rect x="18" y="56" width="14" height="1.6" fill="#1fa3de"/><rect x="32" y="56" width="10" height="1.6" fill="#1b5f9a"/><rect x="42" y="56" width="8" height="1.6" fill="#8a8a8a"/>
    <rect x="18" y="61" width="10" height="1.6" fill="#1fa3de"/><rect x="28" y="61" width="12" height="1.6" fill="#1b5f9a"/><rect x="40" y="61" width="6" height="1.6" fill="#8a8a8a"/>
    <rect x="18" y="66" width="16" height="1.6" fill="#1fa3de"/><rect x="34" y="66" width="6" height="1.6" fill="#1b5f9a"/><rect x="40" y="66" width="10" height="1.6" fill="#8a8a8a"/>
    <rect x="18" y="71" width="12" height="1.6" fill="#1fa3de"/><rect x="30" y="71" width="8" height="1.6" fill="#1b5f9a"/><rect x="38" y="71" width="12" height="1.6" fill="#8a8a8a"/></g>
    <g fill="none" stroke-width="3" transform="rotate(-90 89 67)"><circle cx="89" cy="67" r="8" stroke="#1fa3de" stroke-dasharray="35 50.3"/><circle cx="89" cy="67" r="8" stroke="#1b5f9a" stroke-dasharray="15.3 50.3" stroke-dashoffset="-35"/></g>
  </svg>
  <div class="abs h" style="left:122px;top:58px;font-size:2px">Live Profit &amp; Net Sales</div>
  <div class="abs" style="left:122px;top:62px;font-size:2px;line-height:2.8px;color:var(--blue)">Net Profit<br><b>$55.432M</b><br>Sales = 400,000</div>
  <div class="footbar"></div><div class="brand">VeroTide</div><div class="page">PAGE | 24</div>
</section>

<!-- 25 Dashboard 02 -->
<section class="slide c5 r5">
  <div class="title" style="top:7px">Dashboard 02</div>
  <svg style="left:0;top:0" width="176" height="99" viewBox="0 0 176 99">
    <text x="9" y="26" font-size="1.5" fill="#1fa3de" font-weight="600">Chart Title</text>
    <g fill="#1fa3de"><rect x="15" y="28" width="2.4" height="16"/><rect x="22" y="28" width="2.4" height="16"/><rect x="29" y="28" width="2.4" height="16"/><rect x="36" y="28" width="2.4" height="16"/><rect x="43" y="28" width="2.4" height="16"/><rect x="50" y="28" width="2.4" height="16"/><rect x="57" y="28" width="2.4" height="16"/><rect x="64" y="28" width="2.4" height="16"/><rect x="71" y="28" width="2.4" height="16"/><rect x="78" y="28" width="2.4" height="16"/><rect x="85" y="28" width="2.4" height="16"/></g>
    <line x1="12" y1="44" x2="90" y2="44" stroke="#ccc" stroke-width=".3"/>
    <g transform="translate(143 36)"><circle r="8" fill="#1fa3de"/><path d="M0 0 L0 -8 A8 8 0 0 0 -7 -3.9z" fill="#8a8a8a"/><path d="M0 0 L-7 -3.9 A8 8 0 0 0 -7.6 2.5z" fill="#1b5f9a"/><path d="M0 0 L-7.6 2.5 A8 8 0 0 0 -5 6.2z" fill="#5d5d5d"/></g>
    <g><rect x="10" y="55" width="34" height="16" fill="#f4f8fb"/><polygon points="11,70 11,64 19,60 27,65 35,58 43,62 43,70" fill="#1fa3de"/><polygon points="11,70 11,67 19,65 27,68 35,63 43,66 43,70" fill="#1b5f9a"/>
    <rect x="52" y="55" width="34" height="16" fill="#f4f8fb"/><polygon points="53,70 53,63 61,61 69,64 77,57 85,60 85,70" fill="#1fa3de"/><polygon points="53,70 53,67 61,66 69,67 77,63 85,65 85,70" fill="#1b5f9a"/>
    <rect x="94" y="55" width="34" height="16" fill="#f4f8fb"/><polygon points="95,70 95,62 103,63 111,60 119,64 127,58 127,70" fill="#1fa3de"/><polygon points="95,70 95,67 103,67 111,65 119,68 127,64 127,70" fill="#1b5f9a"/>
    <rect x="136" y="55" width="34" height="16" fill="#f4f8fb"/><polygon points="137,70 137,64 145,59 153,62 161,58 169,61 169,70" fill="#1fa3de"/><polygon points="137,70 137,68 145,65 153,66 161,64 169,66 169,70" fill="#1b5f9a"/></g>
  </svg>
  <div class="footbar"></div><div class="brand">VeroTide</div><div class="page">PAGE | 25</div>
</section>

<!-- 26 Dashboard 03 -->
<section class="slide c1 r6">
  <div class="title" style="top:7px">Dashboard 03</div>
  <svg style="left:0;top:0" width="176" height="99" viewBox="0 0 176 99">
    <g font-size="1.6" fill="#1fa3de" font-weight="600" text-anchor="middle"><text x="50" y="19">Chart Title</text><text x="134" y="23">Chart Title</text><text x="50" y="55">Chart Title</text></g>
    <g stroke="#e3e3e3" stroke-width=".3"><line x1="10" y1="24" x2="84" y2="24"/><line x1="10" y1="30" x2="84" y2="30"/><line x1="10" y1="36" x2="84" y2="36"/><line x1="10" y1="42" x2="84" y2="42"/></g>
    <polyline points="12,30 26,34 40,24 54,36 68,28 82,38" fill="none" stroke="#1b5f9a" stroke-width=".5"/>
    <polyline points="12,38 26,28 40,36 54,30 68,38 82,27" fill="none" stroke="#8a8a8a" stroke-width=".5"/>
    <g fill="#1fa3de"><rect x="108" y="26" width="40" height="1.6"/><rect x="108" y="30" width="34" height="1.6"/><rect x="108" y="34" width="28" height="1.6"/><rect x="108" y="38" width="38" height="1.6"/><rect x="108" y="42" width="22" height="1.6"/></g>
    <g fill="#8a8a8a"><rect x="108" y="27.7" width="30" height=".9"/><rect x="108" y="31.7" width="24" height=".9"/><rect x="108" y="35.7" width="34" height=".9"/><rect x="108" y="39.7" width="20" height=".9"/></g>
    <line x1="10" y1="84" x2="86" y2="84" stroke="#ccc" stroke-width=".3"/>
    <g><rect x="14" y="70" width="2" height="14" fill="#8a8a8a"/><rect x="16.5" y="74" width="2" height="10" fill="#1fa3de"/><rect x="19" y="76" width="2" height="8" fill="#1b5f9a"/>
    <rect x="33" y="64" width="2" height="20" fill="#8a8a8a"/><rect x="35.5" y="72" width="2" height="12" fill="#1fa3de"/><rect x="38" y="75" width="2" height="9" fill="#1b5f9a"/>
    <rect x="52" y="72" width="2" height="12" fill="#8a8a8a"/><rect x="54.5" y="66" width="2" height="18" fill="#1fa3de"/><rect x="57" y="77" width="2" height="7" fill="#1b5f9a"/>
    <rect x="71" y="68" width="2" height="16" fill="#8a8a8a"/><rect x="73.5" y="62" width="2" height="22" fill="#1fa3de"/><rect x="76" y="73" width="2" height="11" fill="#1b5f9a"/></g>
    <circle cx="108" cy="66" r="4" fill="#1fa3de"/><rect x="106.4" y="64" width="3.2" height="4" fill="none" stroke="#fff" stroke-width=".4"/>
  </svg>
  <div class="abs h" style="left:114px;top:62px;font-size:4.2px">436.00</div>
  <div class="abs p" style="left:104px;top:72px;width:46px">Average monthly spend per business customer across all plans.</div>
  <div class="footbar"></div><div class="brand">VeroTide</div><div class="page">PAGE | 26</div>
</section>

<!-- 27 Dashboard 04 -->
<section class="slide c2 r6">
  <div class="title" style="top:7px">Dashboard 04</div>
  <svg style="left:0;top:0" width="176" height="99" viewBox="0 0 176 99">
    <text x="64" y="19" font-size="1.6" fill="#1fa3de" font-weight="600" text-anchor="middle">Chart Title</text>
    <g stroke="#e3e3e3" stroke-width=".3"><line x1="12" y1="22" x2="120" y2="22"/><line x1="12" y1="30" x2="120" y2="30"/><line x1="12" y1="38" x2="120" y2="38"/><line x1="12" y1="46" x2="120" y2="46"/></g>
    <polygon points="12,46 12,26 40,25 70,27 100,22 120,20 120,46" fill="#8a8a8a"/>
    <polygon points="12,46 12,31 40,33 70,33 100,38 120,36 120,46" fill="#1fa3de"/>
    <text x="64" y="58" font-size="1.6" fill="#1fa3de" font-weight="600" text-anchor="middle">Chart Title</text>
    <g fill="#1fa3de"><rect x="20" y="61" width="80" height="1.4"/><rect x="20" y="66" width="70" height="1.4"/><rect x="20" y="71" width="88" height="1.4"/><rect x="20" y="76" width="64" height="1.4"/></g>
    <g fill="#1b5f9a"><rect x="20" y="62.8" width="60" height="1"/><rect x="20" y="67.8" width="76" height="1"/><rect x="20" y="72.8" width="50" height="1"/><rect x="20" y="77.8" width="82" height="1"/></g>
  </svg>
  <div class="stat" style="left:128px;top:24px;width:24px;height:8px;padding:1px 2px;font-size:1.6px;line-height:2.1px"><b>200</b>Sales</div>
  <div class="stat" style="left:128px;top:37px;width:24px;height:8px;padding:1px 2px;font-size:1.6px;line-height:2.1px"><b>40</b>New Clients</div>
  <div class="stat" style="left:128px;top:50px;width:24px;height:8px;padding:1px 2px;font-size:1.6px;line-height:2.1px;background:var(--blue);color:#fff"><b style="color:#fff">14</b>Employees</div>
  <div class="abs" style="left:128px;top:65px;width:42px"><div class="h" style="font-size:2px">Title</div><div class="p">Sales, new clients and staff numbers for this quarter, shown against the same period last year.</div></div>
  <div class="footbar"></div><div class="brand">VeroTide</div><div class="page">PAGE | 27</div>
</section>

<!-- 28 Thank You -->
<section class="slide c3 r6 redbg">
  <div class="thanks">THANK YOU</div>
  <div class="thanks-p">Thank you for your time. We look forward to building fast, secure and reliable networks for your business with the VeroTide group and our companies.</div>
  <div class="brand">VeroTide</div>
</section>

<!-- 29 Icons -->
<section class="slide c4 r6">
  <svg style="left:0;top:0" width="176" height="99" viewBox="0 0 176 99" fill="none" stroke="#1fa3de" stroke-width=".45" stroke-linecap="round" stroke-linejoin="round">
    <g transform="translate(22 15)"><circle r="2.4"/><circle r="1"/></g>
    <g transform="translate(54 15)"><rect x="-1.8" y="-2.4" width="3.6" height="4.8"/><path d="M-1 -1 h2 M-1 0 h2 M-1 1 h1.4"/></g>
    <g transform="translate(87 15)"><circle r="2.4"/><path d="M-2.4 0 h4.8 M0 -2.4 c-1.4 1.5 -1.4 3.3 0 4.8 c1.4 -1.5 1.4 -3.3 0 -4.8"/></g>
    <g transform="translate(120 15)"><circle cx="-1" cy="-1" r="1.2"/><circle cx="1.4" cy="1" r="1.2"/></g>
    <g transform="translate(152 15)"><rect x="-2.2" y="-1.4" width="4.4" height="3.4" rx=".6"/><path d="M-1 -1.4 v-.8 h2 v.8"/></g>

    <g transform="translate(22 31)"><circle r="2.4"/><path d="M0 -1.4 v1.4 l1 .8"/></g>
    <g transform="translate(54 31)"><circle r="1.4"/><path d="M0 -2.6 v.8 M0 1.8 v.8 M-2.6 0 h.8 M1.8 0 h.8"/></g>
    <g transform="translate(87 31)"><rect x="-2.2" y="-1.8" width="4.4" height="3" rx=".5"/><path d="M-.6 1.2 l-.6 1.2 1.4 -1.2"/></g>
    <g transform="translate(120 31)"><circle cy="-.4" r="1.6"/><path d="M-.6 1.4 v.9 h1.2 v-.9"/></g>
    <g transform="translate(152 31)"><path d="M-2.2 -.8 h1.2 l2.6 -1.6 v4.8 l-2.6 -1.6 h-1.2z"/></g>

    <g transform="translate(22 47)"><circle r="2.4"/><path d="M-1 0 l.8 .8 1.4 -1.6"/></g>
    <g transform="translate(54 47)"><circle cy="-.4" r="1.4"/><path d="M-.5 1.2 h1 M0 -2.6 v-.5 M-2.2 -.4 h-.5 M2.2 -.4 h.5"/></g>
    <g transform="translate(87 47)" fill="#1fa3de" stroke="none"><circle cx="-1.2" cy="-1" r=".9"/><circle cx="1.2" cy="-1" r=".9"/><rect x="-2.3" y=".2" width="2.2" height="1.8" rx=".6"/><rect x=".1" y=".2" width="2.2" height="1.8" rx=".6"/></g>
    <g transform="translate(120 47)"><path d="M-1.8 -2 c-.6 1.8 1.8 4.2 3.6 3.6 l.2 -1 -1.2 -.7 -.6 .5 c-.8 -.3 -1.4 -.9 -1.7 -1.7 l.5 -.6 -.7 -1.2z"/></g>
    <g transform="translate(152 47)"><path d="M-2.4 .6 c.6 -2.4 4.2 -2.4 4.8 0 M-1.4 .6 v1 M1.4 .6 v1 M0 -.6 v2.2"/></g>

    <g transform="translate(22 63)"><path d="M-2 2 v-1.4 M-.7 2 v-2.4 M.6 2 v-3.2 M1.9 2 v-4"/></g>
    <g transform="translate(54 63)"><rect x="-1.8" y="-2.4" width="3.6" height="4.8"/><path d="M-.8 .4 l.6 .6 1.2 -1.4"/></g>
    <g transform="translate(87 63)"><path d="M0 -2.4 l2 .8 v1.6 c0 1.4 -1 2.2 -2 2.6 c-1 -.4 -2 -1.2 -2 -2.6 v-1.6z M-.8 0 l.6 .6 1.2 -1.2"/></g>
    <g transform="translate(120 63)" fill="#1fa3de" stroke="none"><circle cy="-1.2" r=".9"/><circle cx="-1.8" cy="-.6" r=".7"/><circle cx="1.8" cy="-.6" r=".7"/><rect x="-1" y="0" width="2" height="2" rx=".6"/><rect x="-2.6" y=".4" width="1.6" height="1.4" rx=".5"/><rect x="1" y=".4" width="1.6" height="1.4" rx=".5"/></g>
    <g transform="translate(152 63)"><circle r="1"/><circle r="2.2" stroke-dasharray="1 .7"/></g>

    <g transform="translate(22 79)"><path d="M-2 -2 h1.4 l1 1 v3 M-.6 .4 h2.4 v1.6 h-2.4"/></g>
    <g transform="translate(54 79)"><polygon points="0,-2.4 2.2,-1.2 2.2,1.2 0,2.4 -2.2,1.2 -2.2,-1.2"/><path d="M0 -2.4 v4.8"/></g>
    <g transform="translate(87 79)"><path d="M0 2.4 c-1.8 -2 -2 -2.8 -2 -3.4 a2 2 0 0 1 4 0 c0 .6 -.2 1.4 -2 3.4z"/><circle cy="-1" r=".7"/></g>
    <g transform="translate(120 79)"><rect x="-2.4" y="-1.6" width="4.8" height="3.2"/><path d="M-2.4 -1.6 l2.4 1.8 2.4 -1.8"/></g>
    <g transform="translate(152 79)"><rect x="-1.8" y="-.4" width="3.6" height="2.6" rx=".4"/><path d="M-1 -.4 v-1 a1 1 0 0 1 2 0 v1"/></g>
  </svg>
  <div class="footbar"></div><div class="brand">VeroTide</div><div class="page">PAGE | 29</div>
</section>

</body>
</html>
```